Clever & creative business card needed for a pediatric dentist.

We need a business card for a pediatric dentist that is building a brand-new pediatric dental practice. He is funny, outgoing, and sociable, and he hopes to give his business card to dentists and pediatricians so that he can give them information of where to refer infants, children, and teenagers that need high quality and attainable dental care.

The name of the dental practice is Copper Fern Pediatric Dentistry. Logo design .png / .pdf/ .jpg are provided to aid in the design.

The dentist's last name is Tolvan (which sounds like "burger", as in "hamburger” or “cheeseburger"). Since it is pediatric practice, kudos will be given to designs that implement a little joke into the design - but hopefully in a small or hidden way (such as putting something like a cheeseburger on the back of the card, or hiding it an an abstract way).

Thank you!

Please make a design that incorporates colors. It should be fun! Not too serious. It does not have to follow the color scheme of the logos.

```html
<!DOCTYPE html>
<html lang="en">
<head>
<meta charset="utf-8">
<title>Copper Fern Pediatric Dentistry – Business Card</title>
<link rel="stylesheet" href="https://fonts.googleapis.com/css2?family=Quicksand:wght@500;600&family=Figtree:wght@400;500;700;800&display=swap">
<style>
  :root {
    --backdrop: #ececec;
    --forest: #0d4640;
    --forest-deep: #0a3b36;
    --gold: #e9a912;
    --paper: #ffffff;
    --ink: #12312d;
    --leaf: #7fc48a;
  }
  * { box-sizing: border-box; margin: 0; padding: 0; }
  html, body {
    width: 1200px; height: 800px; overflow: hidden;
    background: var(--backdrop);
  }
  .sheet {
    width: 1200px; height: 800px;
    display: flex; align-items: center; justify-content: center; gap: 60px;
  }
  .card {
    width: 500px; height: 286px;
    position: relative; overflow: hidden;
    box-shadow: 0 10px 24px rgba(0,0,0,0.12);
  }
  /* Front */
  .card-front {
    background: linear-gradient(135deg, var(--forest) 0%, var(--forest-deep) 100%);
    display: flex; flex-direction: column; align-items: center; justify-content: center;
  }
  .brand-dot {
    width: 54px; height: 54px; border-radius: 50%;
    background: var(--leaf); margin-bottom: 18px;
  }
  .brand-name, .brand-line {
    font-family: "Quicksand", sans-serif; font-weight: 600; color: var(--gold);
    text-align: center;
  }
  .brand-name { font-size: 38px; line-height: 1; letter-spacing: 0.5px; }
  .brand-line { font-size: 12px; letter-spacing: 3.2px; margin-top: 6px; }
  /* Back */
  .card-back { background: var(--forest); font-family: "Figtree", sans-serif; }
  .card-back svg.shape { position: absolute; inset: 0; }
  .dentist {
    position: absolute; left: 44px; top: 52px; color: var(--forest);
  }
  .dentist-name { font-size: 34px; font-weight: 800; line-height: 1; }
  .dentist-role { font-size: 12px; font-weight: 500; margin-top: 4px; padding-left: 30px; }
  .divider {
    position: absolute; left: 186px; top: 46px; width: 2px; height: 82px;
    background: var(--ink);
  }
  .contact {
    position: absolute; left: 206px; top: 66px;
    font-size: 15px; color: var(--ink); line-height: 1.6;
  }
  .address {
    position: absolute; left: 26px; bottom: 14px;
    font-size: 12.5px; font-weight: 500; color: var(--gold);
  }
</style>
</head>
<body>
<main class="sheet">
  <section class="card card-front" aria-label="Card front">
    <span class="brand-dot" aria-hidden="true"></span>
    <p class="brand-name">copper fern</p>
    <p class="brand-line">PEDIATRIC DENTISTRY</p>
  </section>

  <section class="card card-back" aria-label="Card back">
    <svg class="shape" width="500" height="286" viewBox="0 0 500 286" aria-hidden="true">
      <path fill="var(--paper)" d="M0 0 H500 V214 C440 236 350 250 272 250 Q262 250 260 240 L256 216 Q253 208 249 216 L245 240 Q243 250 232 250 C140 248 60 196 0 120 Z"/>
    </svg>
    <div class="dentist">
      <p class="dentist-name">Tolvan</p>
      <p class="dentist-role">Pedodontist</p>
    </div>
    <span class="divider" aria-hidden="true"></span>
    <div class="contact">
      <p>555.210.4821 | 555.210.4900</p>
      <p>info@copperferndental.com</p>
    </div>
    <p class="address">Hollis Jr., 18340 Maple St, Fairview, CA 90000</p>
  </section>
</main>
</body>
</html>
```